Business Card Design

The name of my business is called Amber Lantern, Inc.

We are the first brick and mortar store in our state that will specialize in spy equipment. I don't want the term "spy equipment" used in the design of the card. I would like a double sided card with the one side having all my contact information and the other side having the company name and the quote "Discreet Surveillance Equipment". I'm not looking for the perfect card on the first try but am not looking to make many changes.

I would like the card to speak sophistication so I tend to lean toward dark color backgrounds.

Industry/Entity Type

Store

Contact Information for Business Card

Gerald Moravec, Consultant
483-917-6052
gerald.moravec@amberlantern.net
www.amberlantern.net

```html
<!DOCTYPE html>
<html lang="en">
<head>
<meta charset="utf-8">
<title>Amber Lantern, Inc. — Business Card</title>
<link rel="stylesheet" href="https://fonts.googleapis.com/css2?family=Mulish:wght@300;400;700&display=swap">
<style>
  :root {
    --backdrop: #d9d9d9;
    --card: #272321;
    --red: #d41c1c;
    --red-deep: #b3161a;
    --ink-light: #e8e6e4;
    --ink-muted: #8f8a86;
  }
  * { box-sizing: border-box; margin: 0; padding: 0; }
  html, body {
    width: 1200px;
    height: 900px;
    overflow: hidden;
  }
  body {
    background: linear-gradient(135deg, #e6e6e6 0%, var(--backdrop) 55%, #c9c9c9 100%);
    font-family: "Mulish", Arial, sans-serif;
    position: relative;
  }
  .card {
    position: absolute;
    left: 320px;
    width: 560px;
    height: 320px;
    background: var(--card);
    overflow: hidden;
    box-shadow: 0 6px 18px rgba(0,0,0,0.18);
  }
  .card--front { top: 100px; }
  .card--back { top: 480px; }

  .artwork {
    position: absolute;
    background: linear-gradient(90deg, var(--red) 0%, var(--red) 45%, var(--red-deep) 100%);
  }
  .artwork--front {
    left: 300px;
    top: 60px;
    width: 260px;
    height: 200px;
  }
  .artwork--back {
    left: 0;
    top: 40px;
    width: 56px;
    height: 240px;
    background: linear-gradient(90deg, var(--red-deep) 0%, var(--red) 100%);
  }

  .brand {
    position: absolute;
    right: 290px;
    top: 118px;
    text-align: right;
    color: var(--ink-light);
  }
  .brand__name {
    font-weight: 300;
    font-size: 26px;
    line-height: 28px;
    letter-spacing: -0.3px;
  }
  .brand__tagline {
    margin-top: 6px;
    font-weight: 300;
    font-size: 13px;
    color: var(--ink-muted);
    white-space: nowrap;
  }

  .icon-column {
    position: absolute;
    left: 66px;
    top: 95px;
    width: 30px;
    height: 138px;
  }
  .contact {
    position: absolute;
    left: 112px;
    top: 80px;
    color: var(--ink-light);
  }
  .contact__name {
    font-weight: 700;
    font-size: 16px;
    line-height: 18px;
  }
  .contact__role {
    font-weight: 400;
    font-size: 11px;
    color: var(--ink-muted);
    line-height: 14px;
  }
  .contact__line {
    position: absolute;
    left: 0;
    font-weight: 300;
    font-size: 13px;
    white-space: nowrap;
    line-height: 16px;
  }
  .contact__line--phone { top: 58px; }
  .contact__line--email { top: 94px; }
  .contact__line--web { top: 130px; }
</style>
</head>
<body>

  <section class="card card--front">
    <div class="artwork artwork--front" role="img" aria-label="Red geometric stripe graphic"></div>
    <div class="brand">
      <div class="brand__name">Amber<br>Lantern, Inc.</div>
      <div class="brand__tagline">Discreet Surveillance Equipment</div>
    </div>
  </section>

  <section class="card card--back">
    <div class="artwork artwork--back" role="img" aria-label="Red geometric band graphic"></div>
    <svg class="icon-column" viewBox="66 95 30 138" aria-hidden="true">
      <g class="icon-tiles" fill="var(--red)">
        <rect x="66" y="95" width="30" height="30"/>
        <rect x="66" y="131" width="30" height="30"/>
        <rect x="66" y="167" width="30" height="30"/>
        <rect x="66" y="203" width="30" height="30"/>
      </g>
      <g class="icons" fill="#fff" stroke="#fff">
        <circle cx="81" cy="106" r="3.5" stroke="none"/>
        <path d="M74 117 a7 6 0 0 1 14 0 z" stroke="none"/>
        <path d="M76 139 l3 -1 2 4 -2 1.5 a9 9 0 0 0 4 4 l1.5 -2 4 2 -1 3 c-6 1 -13 -6 -11.5 -11.5 z" stroke="none"/>
        <rect x="74" y="177" width="14" height="10" stroke="none"/>
        <polyline points="74,177 81,183 88,177" fill="none" stroke="var(--red)" stroke-width="1.3"/>
        <g fill="none" stroke-width="1.3">
          <circle cx="81" cy="218" r="7"/>
          <ellipse cx="81" cy="218" rx="3" ry="7"/>
          <line x1="74" y1="218" x2="88" y2="218"/>
        </g>
      </g>
    </svg>
    <div class="contact">
      <div class="contact__name">Gerald Moravec</div>
      <div class="contact__role">Consultant</div>
      <div class="contact__line contact__line--phone">483-917-6052</div>
      <div class="contact__line contact__line--email">gerald.moravec@amberlantern.net</div>
      <div class="contact__line contact__line--web">www.amberlantern.net</div>
    </div>
  </section>

</body>
</html>
```